Cosmetics Brand Logo and Bottle Label Design

We are creating a new cosmetics brand called "Nolan Whitby" and would like you to create an amazing logo and bottle label for this brand's new 100% pure argan oil product.
For the logo, we really like the logo's of Marin Calloway and Vessa. The text should be Sans Serif (without feet).
For the actual bottle label, please find attached labels of one of our competitors design which really like. We really like the simplicity and elegance of the design. The only difference is that our product will be using light turqoise as the brand color. Please feel free to add your own creativity into it as well.
Industry/Entity Type
Cosmetics
Logo Text
Nolan Whitby
Font styles to use

```html
<!DOCTYPE html>
<html lang="en">
<head>
<meta charset="utf-8">
<title>Nolan Whitby – Argan Oil Label</title>
<link rel="stylesheet" href="https://fonts.googleapis.com/css2?family=Oswald:wght@400&family=Roboto:wght@300;400&display=swap">
<style>
  :root {
    --mint-bg: #c9e8e1;
    --mint-pattern: #d6eee8;
    --teal: #2bb5a0;
    --ribbon-text: #e4f5f1;
  }
  html, body {
    margin: 0;
    padding: 0;
    overflow: hidden;
  }
  .label {
    position: relative;
    width: 1200px;
    height: 625px;
    overflow: hidden;
    background: var(--mint-bg);
    font-family: "Roboto", Arial, sans-serif;
  }
  .swirl-pattern {
    position: absolute;
    inset: 0;
    background: radial-gradient(ellipse at 50% 50%, var(--mint-pattern) 0%, var(--mint-bg) 75%);
  }
  .ribbon {
    position: absolute;
    left: 0;
    top: 0;
  }
  .ribbon-text {
    position: absolute;
    left: 531px;
    top: 272px;
    width: 470px;
    text-align: center;
    transform: translate(-50%, -50%) rotate(-90deg);
    color: var(--ribbon-text);
  }
  .brand-name {
    margin: 0;
    font-family: "Oswald", "Arial Narrow", sans-serif;
    font-weight: 400;
    font-size: 62px;
    line-height: 56px;
    letter-spacing: 4px;
    text-transform: uppercase;
    white-space: nowrap;
  }
  .product-line {
    margin: 0;
    font-weight: 300;
    font-size: 32px;
    line-height: 36px;
    white-space: nowrap;
  }
  .silhouette {
    position: absolute;
    left: 617px;
    top: 212px;
    width: 120px;
    height: 278px;
    border-radius: 60px 60px 30px 30px;
    background: linear-gradient(180deg, var(--teal), #3cc0ab);
    opacity: 0.9;
  }
  .product-info {
    position: absolute;
    left: 600px;
    margin: 0;
    transform: translateX(-50%);
    color: var(--teal);
    white-space: nowrap;
    text-align: center;
  }
  .descriptor {
    top: 522px;
    font-size: 21px;
    line-height: 26px;
  }
  .volume {
    top: 555px;
    font-size: 32px;
    line-height: 38px;
  }
</style>
</head>
<body>
  <main class="label">
    <div class="swirl-pattern" role="img" aria-label="Soft swirling wave pattern in pale mint covering the background"></div>

    <svg class="ribbon" width="1200" height="625" viewBox="0 0 1200 625" aria-hidden="true">
      <polygon points="460,0 596,0 596,506 528,478 460,506" fill="var(--teal)"/>
    </svg>

    <div class="ribbon-text">
      <h1 class="brand-name">Nolan Whitby</h1>
      <p class="product-line">100% pure argan oil</p>
    </div>

    <div class="silhouette" role="img" aria-label="Teal profile silhouette of a woman with long flowing hair"></div>

    <p class="product-info descriptor">organic moisturizing oil</p>
    <p class="product-info volume">50mL 1.7 fl oz</p>
  </main>
</body>
</html>
```